Corrimbel Lodge Web Design Project

I am looking for a striking, modern and user friendly site to promote my business, Corrimbel Lodge.

Corrimbel Lodge comprises of 3 elements : Restaurant, Resort and Events and the site must showcase all of these.
Updates

Project Deadline Extended
Reason: Too far away from brief ! Please check out the 2 website links to restaurant sites i LOVE for inspiration ! I am happy to pay for a quality designer and also for anyone that can code this !

Target Market(s)

Our Restaurant clientele demographic is 30-60 years old and are a mix of locals and tourists. The Restaurant is very much a destination venue so we attract people that wish to seek out amazing food.

The Event side of things attracts mainly weddings, this is a lucrative arm of the business and this side of the site must also be outstanding.

The Resort comprises of 7 boutique loft apartment and has a big pool and spa. We attract a mix of locals but want to push it as a ' getaway '

Industry/Entity Type

Business

Requirements
Must have
• I would like the first page to be an overall blog and to highlight the 3 area of the business. Lets have the 3 keywords as clickable tabs that take you to that section of the site.

RESTAURANT RESORT EVENTS

The RESTAURANT page should include the following tabs ( i have provided the information to be added to each tab as an example )

MENU ( Breakfast, Lunch, Dinner, Set Menu, Wine List)

FUNCTIONS (Private Dining Room, Exclusive Use, Wine Nights Coming Soon)

RESERVATIONS (Enquiry Form linked to my info@ address, Reservation Policies, Contact Number)

GALLERY & PRESS ( Press Articles, Latest News, What's On, Photo's, Wedding Hot Spot)

CONTACT US (Opening Times, Map, Contact Details, Sign Up For Our Newsletter, Sharely Link )

The RESORT page should include the following tabs :
# LOFTS & RATES
# FACILITIES
# SPECIAL OFFERS
# GALLERY
# RESERVATIONS

The EVENTS page should include the following tabs :
# WEDDINGS
# CONFERENCES
# PRIVATE EVENTS
# GALLERY
# ENQUIRY FORM
Nice to have
• Include Logo, good branding

```html
<!DOCTYPE html>
<html lang="en">
<head>
<meta charset="utf-8">
<title>Corrimbel Lodge — Restaurant, Resort, Events</title>
<link href="https://fonts.googleapis.com/css2?family=Crete+Round&family=Open+Sans:wght@400;600&display=swap" rel="stylesheet">
<style>
:root{
  --wall-top:#5a4634;
  --wall-mid:#6e5a45;
  --wall-dark:#3a2d22;
  --floor:#17120e;
  --paper:#f4ebdc;
  --paper-edge:#e9dcc6;
  --card-top:#efdcbc;
  --card-bottom:#d6c1a1;
  --brown:#6b3a22;
  --btn-top:#6a3a24;
  --btn-bottom:#3b1d10;
  --ink:#2b2420;
  --meta:#3a3633;
  --icon:#4a4644;
  --rule:#b7a993;
  --white:#ffffff;
}
*{margin:0;padding:0;box-sizing:border-box}
html,body{width:1200px;height:1000px;overflow:hidden}
body{position:relative;background:var(--floor);font-family:Arial,Helvetica,sans-serif;color:var(--ink)}
.backdrop{position:absolute;left:0;top:0;width:1200px;height:612px;
  background:radial-gradient(ellipse at 50% 35%,var(--wall-mid) 0%,var(--wall-top) 45%,var(--wall-dark) 100%)}
.backdrop-beam{position:absolute;left:0;top:0;width:1200px;height:38px;background:linear-gradient(#0a0910,#2a2320 70%,#8c7b68)}
.brand{position:absolute;left:503px;top:0;width:248px;height:163px;background:linear-gradient(#ffffff,#ececec);border-radius:0 0 14px 14px}
.brand-mark{position:absolute;left:94px;top:28px;width:60px;height:60px;border:3px solid var(--ink)}
.brand-name{position:absolute;left:34px;top:109px;width:186px;height:50px;background:var(--btn-bottom);color:var(--white);
  font-family:Arial,Helvetica,sans-serif;font-size:23px;line-height:26px;padding-top:4px;border-radius:4px;text-align:center}
.brand-tag{display:block;font-size:11px;line-height:14px}
.panel{position:absolute;left:156px;top:197px;width:940px;height:733px;background:var(--paper);border-radius:10px;
  box-shadow:0 0 0 2px var(--paper-edge) inset}
.panel::before,.panel::after{content:"";position:absolute;left:0;right:0;height:1px;background:#e2d6c3}
.panel::before{top:29px}.panel::after{top:704px}
.service{position:absolute;top:47px;width:221px;height:291px;background:linear-gradient(var(--card-top),var(--card-bottom));text-align:center}
.service-icon{display:block;margin:14px auto 0;width:106px;height:106px}
.service-title{font-family:"Crete Round",serif;font-size:26px;font-weight:400;color:var(--brown);letter-spacing:2px;margin-top:12px;line-height:30px}
.service-text{font-size:12.5px;line-height:18px;color:var(--ink);padding:0 16px;margin-top:2px}
.read-more{display:inline-block;margin-top:13px;width:119px;height:36px;line-height:34px;border-radius:5px;border:1px solid #2a150b;
  background:linear-gradient(var(--btn-top),var(--btn-bottom));color:var(--white);font-family:"Open Sans",sans-serif;font-size:17px;text-decoration:none}
.blog-heading{position:absolute;left:85px;top:374px;font-family:"Crete Round",serif;font-size:30px;font-weight:400;color:var(--ink);letter-spacing:1px}
.blog-rule{position:absolute;left:85px;top:416px;width:759px;border-top:2px dashed var(--rule)}
.post-frame{position:absolute;left:82px;top:451px;width:209px;height:189px;background:#e2cfb2;padding:8px 6px 8px 7px}
.post-photo{width:196px;height:173px;background:radial-gradient(ellipse at 50% 20%,#e9c26d,#9a6a33 45%,#4a3524 80%)}
.post{position:absolute;left:308px;top:446px;width:545px}
.post-title{font-family:"Crete Round",serif;font-size:21px;font-weight:400;color:var(--brown)}
.post-meta{display:flex;margin-top:6px;font-size:12.5px;letter-spacing:0.6px;color:var(--meta);text-transform:uppercase;align-items:center}
.meta-item{display:flex;align-items:center;gap:6px;margin-right:26px}
.meta-item svg{width:19px;height:19px}
.post-body{margin-top:8px;font-size:12.5px;line-height:20px;color:var(--ink)}
.post-body p{margin-bottom:20px}
.share{position:absolute;left:540px;top:629px;display:flex;gap:6px;font-size:10px}
.share-btn{display:flex;align-items:center}
.share-label{height:19px;line-height:17px;padding:0 6px;border:1px solid #c9c0b6;border-radius:3px;background:#fbfbfb;color:#333;font-weight:bold}
.share-label.primary{background:#4b64a0;color:#fff;border-color:#3b5290;width:60px;text-align:center}
.share-count{height:17px;line-height:15px;padding:0 5px;border:1px solid #c9c0b6;background:#fff;margin-left:3px;border-radius:2px;color:#333}
.footer{position:absolute;left:0;top:954px;width:1200px;text-align:center;color:var(--white);font-size:12.5px;font-weight:bold}
</style>
</head>
<body>
<div class="backdrop" role="img" aria-label="Textured dark brown wall backdrop"></div>
<div class="backdrop-beam"></div>

<header class="brand">
  <div class="brand-mark"></div>
  <div class="brand-name">Corrimbel Lodge<span class="brand-tag">restaurant - resort - events</span></div>
</header>

<main class="panel">
  <section class="service" style="left:93px">
    <svg class="service-icon" viewBox="0 0 106 106" aria-hidden="true">
      <circle cx="53" cy="53" r="52" fill="#050505"/>
      <g fill="#fff">
        <rect x="30" y="30" width="3" height="18"/><rect x="35" y="30" width="3" height="18"/><rect x="40" y="30" width="3" height="18"/>
        <rect x="29" y="46" width="15" height="6" rx="3"/><rect x="34.5" y="50" width="4" height="34" rx="2"/>
        <path d="M52 24 q8 10 6 30 h-4 v30 h-4 z"/>
        <ellipse cx="71" cy="38" rx="7" ry="12"/><rect x="69" y="46" width="4" height="38" rx="2"/>
      </g>
    </svg>
    <h2 class="service-title">Restaurant</h2>
    <p class="service-text">simply dummy text of the printing and typesetting industry. Lorem Ipsum has industry.</p>
    <a class="read-more" href="#restaurant">Read More</a>
  </section>
  <section class="service" style="left:360px;top:48px">
    <svg class="service-icon" viewBox="0 0 106 106" aria-hidden="true">
      <circle cx="53" cy="53" r="52" fill="#050505"/>
      <g fill="#fff">
        <path d="M24 52 L53 30 L82 52 L78 56 L53 37 L28 56 Z"/>
        <rect x="32" y="53" width="42" height="22"/>
      </g>
      <rect x="38" y="58" width="9" height="9" fill="#050505"/><rect x="59" y="58" width="9" height="9" fill="#050505"/>
      <rect x="49" y="62" width="8" height="13" fill="#050505"/>
    </svg>
    <h2 class="service-title">Resort</h2>
    <p class="service-text">simply dummy text of the printing and typesetting industry. Lorem Ipsum has industry.</p>
    <a class="read-more" href="#resort">Read More</a>
  </section>
  <section class="service" style="left:619px">
    <svg class="service-icon" viewBox="0 0 106 106" aria-hidden="true">
      <circle cx="53" cy="53" r="52" fill="#050505"/>
      <rect x="30" y="30" width="46" height="46" rx="4" fill="none" stroke="#fff" stroke-width="4"/>
      <rect x="30" y="30" width="46" height="10" fill="#fff"/>
      <rect x="38" y="24" width="4" height="12" fill="#fff"/><rect x="64" y="24" width="4" height="12" fill="#fff"/>
      <g fill="#fff">
        <rect x="36" y="45" width="7" height="6"/><rect x="46" y="45" width="7" height="6"/><rect x="56" y="45" width="7" height="6"/><rect x="66" y="45" width="5" height="6"/>
        <rect x="36" y="55" width="7" height="6"/><rect x="46" y="55" width="7" height="6"/><rect x="56" y="55" width="7" height="6"/><rect x="66" y="55" width="5" height="6"/>
        <rect x="36" y="65" width="7" height="6"/><rect x="46" y="65" width="7" height="6"/><rect x="56" y="65" width="7" height="6"/>
      </g>
    </svg>
    <h2 class="service-title">Events</h2>
    <p class="service-text">simply dummy text of the printing and typesetting industry. Lorem Ipsum has industry.</p>
    <a class="read-more" href="#events">Read More</a>
  </section>

  <h2 class="blog-heading">Blog</h2>
  <div class="blog-rule"></div>

  <div class="post-frame"><div class="post-photo" role="img" aria-label="Restaurant dining room with warm ceiling lights"></div></div>
  <article class="post">
    <h3 class="post-title">Dr. Maple’s Garden Table (best apps)</h3>
    <div class="post-meta">
      <span class="meta-item"><svg viewBox="0 0 19 19"><circle cx="9.5" cy="9.5" r="9.5" fill="var(--icon)"/><rect x="6" y="5" width="7" height="9" fill="#fff"/></svg>April 20, 2013</span>
      <span class="meta-item"><svg viewBox="0 0 19 19"><circle cx="9.5" cy="9.5" r="9.5" fill="var(--icon)"/><circle cx="9.5" cy="7.5" r="2.6" fill="#fff"/><path d="M5 14 q4.5-6 9 0z" fill="#fff"/></svg>Admin</span>
      <span class="meta-item"><svg viewBox="0 0 19 19"><circle cx="9.5" cy="9.5" r="9.5" fill="var(--icon)"/><ellipse cx="8" cy="8.5" rx="3.5" ry="2.6" fill="#fff"/><ellipse cx="11.5" cy="11" rx="3" ry="2.2" fill="#fff"/></svg>0 Comments</span>
    </div>
    <div class="post-body">
      <p>Welcome! Have a look around but we’re still under construction! We’ll have a full launch soon! the meantime, please subscribe to options in the right column to be notified when the site is finished.</p>
      <p>In the meantime, please subscribe to one of our social media options in the right column to be notified when the site is finished.</p>
      <p>Thanks!</p>
    </div>
  </article>
  <div class="share">
    <span class="share-btn"><span class="share-label primary">Sharely</span><span class="share-count">3</span></span>
    <span class="share-btn"><span class="share-label">Plusbox</span><span class="share-count">0</span></span>
    <span class="share-btn"><span class="share-label">Pinly</span><span class="share-count">228</span></span>
    <span class="share-btn"><span class="share-label">Chirp</span><span class="share-count">4</span></span>
  </div>
</main>

<footer class="footer">© 2013 Corrimbel Lodge. All Rights Reserved.</footer>
</body>
</html>
```